Craft Portuguese Gin Distillery launching new gin into international market

We are going to launch two new gins:
1. An aged version of the Velmar Caspo, one that already exists - aged in port casks. This will be a 500ml bottle. Bottle not defined yet - Check www.sipvorlane.com
2. A new gin with a lower ABV (lower strength), to satisfy both connoisseurs and "ordinary"; customers. We want to stay with the branding line. The label must appeal to the customer to try the gin, must stand out on a shelf that is full of other spirits. We want to pass on the idea of a premium gin. No botle selected yet. For this gin we may use only a label or a complete decorated bottle. Take care of the legal demands that have to go onto the label - we can help with this later on.
Notes:
- The distillery's name is Orvane - Premium Spirits (logo attached)
- Our first gin is called Velmar Caspo (logo attached)
- No names selected for either of these gins;
- We have a moto that we would like to see on the bottle:
"Drink to remember, not to forget!";
- Our gins have a unique botanical that is fig tree bark, we are portuguese and we are very fond of the fig image attached.
- Attached we send some documents where you can learn about the story of the gin and also for you to get to know us little better.
- If you wish to suggest a bottle, please look-up these two web sites:
https://www.brolukvessel.com/en
https://www.quandimflask.com/
Please contact us for any further information.
Thank you

Target Market(s)

Spirits worldwide

Colors

Designer to choose colors to be used in the design.

Requirements
Must have
• Mandatory Legal information for spirit drinks
• Place for:
• - Producer / bottler (name and addres)
• - Origin fo the product - Product from Portugal
• - ABV and Capacity
• - Type of product: "Londo Dry Gin"
Nice to have
• - We have a moto that we would like to see on the bottle:
• "quot;Drink to remember, not to forget!";
• - Our gins have a unique botanical that is fig tree bark, we are portuguese and we are very fond of the fig image attached.

```html
<!DOCTYPE html>
<html lang="en">
<head>
<meta charset="utf-8">
<title>Velmar Caspo – London Dry Gin Label</title>
<link rel="stylesheet" href="https://fonts.googleapis.com/css2?family=Bodoni+Moda:wght@500&family=Allura&family=Oswald:wght@400;600&family=Cormorant+Garamond:wght@500&display=swap">
<style>
  :root {
    --page-bg: #ecebe8;
    --label-white: #f7f6f3;
    --fig-beige: #ddd3bd;
    --fig-beige-soft: #ece6d8;
    --band-dark: #312f31;
    --accent-red: #e0574f;
    --text-light: #f3f1ee;
    --text-dark: #2a292b;
  }
  * { box-sizing: border-box; margin: 0; padding: 0; }
  html, body { width: 1200px; height: 800px; overflow: hidden; }
  body { background: var(--page-bg); position: relative; }

  .label-set {
    position: absolute;
    left: 388px;
    top: 30px;
    width: 423px;
    height: 740px;
  }
  .type-strip {
    position: absolute;
    left: 0;
    top: 198px;
    width: 36px;
    height: 327px;
    background: var(--accent-red);
    display: flex;
    align-items: center;
    justify-content: center;
  }
  .type-strip__text {
    transform: rotate(-90deg);
    white-space: nowrap;
    font-family: "Oswald", sans-serif;
    font-weight: 600;
    font-size: 12px;
    letter-spacing: 2px;
    color: var(--text-light);
  }
  .label {
    position: absolute;
    left: 36px;
    top: 0;
    width: 387px;
    height: 740px;
    background: var(--label-white);
    overflow: hidden;
  }
  .label__fig-art {
    position: absolute;
    inset: 0;
    background:
      radial-gradient(ellipse 60% 40% at 70% 22%, var(--fig-beige) 0%, transparent 70%),
      radial-gradient(ellipse 55% 35% at 55% 82%, var(--fig-beige) 0%, transparent 70%),
      linear-gradient(160deg, var(--fig-beige-soft), var(--label-white) 55%, var(--fig-beige-soft));
  }
  .label__band {
    position: absolute;
    left: 0;
    top: 198px;
    width: 334px;
    height: 327px;
    background: var(--band-dark);
    display: flex;
    flex-direction: column;
    align-items: center;
    color: var(--text-light);
  }
  .brand-name {
    margin-top: 58px;
    font-family: "Bodoni Moda", serif;
    font-weight: 500;
    font-size: 40px;
    line-height: 1;
    color: var(--text-light);
  }
  .motto {
    margin-top: 44px;
    font-family: "Allura", cursive;
    font-size: 24px;
    color: var(--text-light);
  }
  .legal {
    margin-top: 22px;
    width: 208px;
    text-align: center;
  }
  .legal__bottler {
    border-top: 1px solid var(--text-light);
    border-bottom: 1px solid var(--text-light);
    padding: 6px 0 4px;
    font-family: "Oswald", sans-serif;
    font-weight: 400;
    font-size: 12px;
    letter-spacing: 1.6px;
  }
  .legal__origin {
    padding-top: 5px;
    font-family: "Cormorant Garamond", serif;
    font-weight: 500;
    font-size: 14px;
    letter-spacing: 0.8px;
  }
  .label__abv {
    position: absolute;
    left: 69px;
    top: 694px;
    font-family: "Oswald", sans-serif;
    font-weight: 600;
    font-size: 15px;
    letter-spacing: 1.5px;
    color: var(--text-dark);
  }
</style>
</head>
<body>
  <div class="label-set">
    <div class="type-strip"><span class="type-strip__text">LONDON DRY GIN</span></div>
    <div class="label">
      <div class="label__fig-art" role="img" aria-label="Engraved fig branch illustration with leaves and fruit in soft beige"></div>
      <div class="label__band">
        <div class="brand-name">Velmar Caspo</div>
        <p class="motto">Drink to Remember, Not to Forget!</p>
        <div class="legal">
          <p class="legal__bottler">BOTTLER NAME - LISBON 2019</p>
          <p class="legal__origin">PRODUCT FROM PORTUGAL</p>
        </div>
      </div>
      <p class="label__abv">58% ABV</p>
    </div>
  </div>
</body>
</html>
```